依頼詳細
<サイトマップ>
①TOPページ
②SALON(店舗情報)
③STAFF(スタッフ紹介)
④STYLE(ギャラリー)
⑤COUPON(クーポン)
⑥FEATURE(当店の特徴)
⑦RECRUIT/COMPANY(求人・会社概要)
⑧BLOG(サイト内ブログ)
⑨NEWS(サイト内ブログ)
⑩MENU(メニュー)
⑪VOICE(お客様の声)
⑫GUEST SNAP(ゲストスナップ)

<デザインテイスト>
・ナチュラル  ・優しい  ・モダン  ・清潔な

<顧客ターゲット>
・女性
・20代~50代
①40代 ②50代 ③20代
・学生、会社員、自営業、未婚、既婚、妊婦、子育て、中年

【競合サイト】
http://www.tintlounge-mirea.j(大阪中心のカラー専門サロン)
http://www.pebble-salon.j(大きいサロン)
http://www.nuvo-ltd.co (北海道で大きいサロン)

【要望】
・pictabookのアイコンをサイト内に配置してください。
・予約が外部のためバナーなどを配置して頂けると嬉しいです。
・「VOICE」ページにはA4サイズのカウンセリングシートなどを
お客様に記入していただいたものを添付する予定ですので、TOpに
新着エリアなどがあってもうれしいです。
・ブログ、新着は新着BOXで配置して頂きたいです。

※素材は追記分内に書いています。
【素材】
■ピクセラ
素材として定期ダウンロードできる画像は使用して頂いて構いません。
その際にカンプ画像でダウンロードしてください。
(画像検索した際に出てくるサムネール下の画像番号の横にピクセラのマーク
があるものは使用不可できません・・・)
その他の素材に関しては、フリーで提供可能なものでお願いします。
■サロン外観・内装写真(ロゴ入り)
http://boxvault-example.jp/get/3f7c2d9a18e6b4c05a7d1e92f6b3c8a4d0e57f21
ダウンロードパスワード kq7vzr2t

すみません、ピクセラのURL添付し忘れてました。
https://jp.pixera-example.com/

宜しくお願いします。
今回、当サロンのコンペに閲覧・ご提案して頂きましたデザイナー様
誠にありがとうございます!!
今でもたくさんのデザイン案を提案して頂いておりますが、もう少し色々なデザイン案を見たいという事もあり、1週間コンペ期間を延長することと致しました。
依頼詳細に囚われず、色みやレイアウトもデザイナー様の自由にデザインして頂いたものをみたいので是非、提案頂ければとても嬉しいです!!
(できれば、入れて頂くページは変えないでほしいです。)
どうぞ、宜しくお願い致します。

シンプルな中にも細部までの細やかなデザインや、デザイナー様のセンスの良さもあってサロンにとてもあったデザインに仕上がっていると思います。
とても満足しています。

今回ご提案していただいたデザイナー様へ
たくさんのデザイン案を度提案頂きまして、誠にありがとうございました。
”カラー専門店”という少し珍しい業態で当サロンの良さをうまく取り入れてくださっている方が多い中で一つに絞るのが中々、大変ではありました。
どれももったいないデザインばかりでした。。。
またこのような機会がございましたら是非ご提案していただければ幸いでございます。
ありがとうございました。

```html
<!DOCTYPE html>
<html lang="ja">
<head>
<meta charset="utf-8">
<title>HUELIA カラー専門サロン</title>
<link href="https://fonts.googleapis.com/css2?family=Cormorant+Garamond:wght@400;600&family=Noto+Sans+JP:wght@400;500;700&family=Noto+Serif+JP:wght@400;600&display=swap" rel="stylesheet">
<style>
:root{
  --ink:#555b5e;
  --ink-soft:#8a9094;
  --teal:#8ccfd2;
  --teal-deep:#5fb3b9;
  --blue:#5d9fc9;
  --sky:#eef7fb;
  --line:#d9e3e6;
  --cream:#f7f4ee;
  --white:#ffffff;
  --accent:#e88fa0;
}
*{margin:0;padding:0;box-sizing:border-box}
html,body{width:1200px;height:4000px;overflow:hidden;background:var(--white)}
body{font-family:"Noto Sans JP",sans-serif;color:var(--ink);font-size:13px;line-height:1.8}
.page{position:relative;width:1200px;height:4000px}
.abs{position:absolute}
.ph{display:block}

/* sidebar */
.sidebar{left:0;top:0;width:220px;height:860px;background:var(--white);border-right:1px solid var(--line)}
.brand{left:24px;top:34px;display:flex;align-items:center;gap:10px}
.brand-mark{width:14px;height:14px;background:var(--teal)}
.brand-name{font-family:"Noto Sans JP",sans-serif;font-size:26px;font-weight:500;letter-spacing:.12em;color:var(--ink);line-height:1}
.brand-sub{left:24px;top:78px;font-size:10px;color:var(--ink-soft);letter-spacing:.1em}
.reserve{left:20px;top:236px;width:180px;height:56px;background:var(--teal);color:var(--white);text-align:center;padding-top:6px}
.reserve b{display:block;font-family:"Cormorant Garamond",serif;font-size:17px;letter-spacing:.05em;line-height:1.5}
.reserve span{font-size:10px}
.nav{left:28px;top:312px;list-style:none}
.nav li{font-family:"Cormorant Garamond",serif;font-size:13px;letter-spacing:.12em;line-height:23px;color:var(--ink)}
.nav li::before{content:"";display:inline-block;width:5px;height:5px;border-radius:50%;background:var(--teal);margin-right:10px;vertical-align:middle}
.side-banner{left:20px;width:180px;height:52px;border:1px solid var(--line);font-size:11px;padding:6px 10px;line-height:1.5}
.side-coupon{top:586px;background:var(--cream)}
.side-coupon b{font-family:"Cormorant Garamond",serif;font-size:20px;color:var(--accent);letter-spacing:.1em;display:block;line-height:1.2}
.side-snap{top:660px;display:flex;gap:8px;align-items:center}
.side-snap .ph{width:50px;height:38px;background:linear-gradient(135deg,#d8c6b3,#9c7f68)}
.side-social{top:764px;height:36px;background:var(--blue);color:var(--white);border:0;padding:7px 12px;display:flex;gap:8px;align-items:center}
.side-social i{width:14px;height:14px;background:var(--white);display:block}

/* hero */
.hero{left:220px;top:0;width:980px;height:600px}
.hero .ph{width:100%;height:100%;background:linear-gradient(100deg,#efe8dd 0%,#e4dbcd 35%,#c9b4a0 62%,#8f6d58 80%,#f1ece6 100%)}
.hero-copy{left:300px;top:44px;font-family:"Noto Serif JP",serif;color:var(--ink)}
.hero-copy p{font-size:22px;line-height:1.7;letter-spacing:.06em}
.hero-copy p.big{font-size:32px;font-weight:600}
.hero-copy em{font-style:normal;color:var(--teal-deep)}
.hero-tag{left:300px;top:248px;background:var(--teal);color:var(--white);font-size:12px;padding:3px 14px;letter-spacing:.05em}
.hero-tel{right:24px;top:560px;background:rgba(255,255,255,.85);padding:2px 14px;font-family:"Cormorant Garamond",serif;font-size:20px;font-weight:600;display:flex;align-items:center;gap:6px}

/* section titles */
.sec-title{width:100%;text-align:center}
.sec-title h2{font-family:"Cormorant Garamond",serif;font-weight:400;font-size:26px;letter-spacing:.2em;color:var(--ink);line-height:1.4}
.sec-title small{display:block;font-size:11px;color:var(--ink-soft);letter-spacing:.1em;line-height:1.2}
.more{width:110px;height:28px;border:1px solid var(--line);background:var(--white);font-size:11px;text-align:center;line-height:26px;color:var(--ink)}
.more::before{content:"▸ ";color:var(--teal-deep)}

/* feature */
.feature{left:220px;top:720px;width:980px}
.feature .lead{margin-top:20px;text-align:center;font-family:"Noto Serif JP",serif;font-size:19px;letter-spacing:.08em}
.feature .body{margin:10px auto 0;width:620px;text-align:center;font-size:12px;color:var(--ink-soft)}
.grid{left:240px;top:960px;width:880px;height:412px;display:grid;grid-template-columns:repeat(4,220px);grid-template-rows:repeat(2,206px)}
.tile{padding:24px 20px;color:var(--white)}
.tile h3{font-family:"Noto Serif JP",serif;font-size:38px;font-weight:400;line-height:1.2}
.tile h3 small{font-size:18px}
.tile p{font-size:11px;line-height:1.7;margin-top:10px}
.t1{background:var(--teal)}.t2{background:#7cc4c2}.t3{background:#93cad8}.t4{background:var(--blue)}
.g1{background:linear-gradient(135deg,#f4f1ec,#bfa592)}
.g2{background:linear-gradient(135deg,#efe9e2,#c8b4a4)}
.g3{background:linear-gradient(135deg,#8b7d5e,#3d3a2c)}
.g4{background:linear-gradient(135deg,#d6c3b0,#7d5c49)}

/* style */
.style{left:220px;top:1540px;width:980px}
.gallery{left:240px;top:1632px;width:880px;display:grid;grid-template-columns:repeat(4,190px);column-gap:40px;row-gap:30px}
.gallery figure .ph{width:190px;height:200px}
.gallery figcaption{font-size:11px;margin-top:6px;text-align:center}
.h1{background:linear-gradient(160deg,#f0ebe5,#a47d68)}
.h2{background:linear-gradient(160deg,#f3eee8,#c09f7c)}
.h3{background:linear-gradient(160deg,#ece5dc,#6f5444)}
.h4{background:linear-gradient(160deg,#ebe4dd,#8a6550)}

/* menu */
.menu-band{left:232px;top:2300px;width:896px;height:430px;background:var(--sky)}
.menu{left:220px;top:2316px;width:980px}
.menu-cols{left:262px;top:2396px;width:836px;display:grid;grid-template-columns:1fr 1fr;column-gap:60px;row-gap:22px}
.menu-block h4{font-size:14px;font-weight:500;border-bottom:1px solid var(--line);padding-bottom:4px;margin-bottom:6px}
.menu-block h4 span{font-size:10px;color:var(--ink-soft);margin-left:8px;font-weight:400}
.row{display:flex;font-size:11px;line-height:22px}
.row span:first-child{flex:none}
.row i{flex:1;border-bottom:1px dotted #b8c4c8;margin:0 6px 7px}
.promo{left:360px;top:2696px;width:640px;height:80px;background:var(--white);border:1px solid var(--teal)}
.promo .badge{left:18px;top:12px;width:56px;height:56px;border-radius:50%;background:var(--teal);color:var(--white);font-size:11px;text-align:center;line-height:1.4;padding-top:11px}
.promo .txt{left:94px;top:12px;font-family:"Noto Serif JP",serif;line-height:1.4}
.promo .txt small{display:block;font-size:11px;color:var(--ink-soft)}
.promo .txt b{font-size:26px;color:var(--teal-deep);font-weight:600}
.promo .off{left:330px;top:14px;font-family:"Cormorant Garamond",serif;font-size:52px;font-weight:600;color:var(--accent);line-height:1}
.promo .off small{font-size:26px}
.promo .note{right:16px;top:14px;width:120px;font-size:10px;line-height:1.5;color:var(--ink-soft);border:1px dashed var(--teal);padding:4px 6px}

/* news blog */
.box{top:2940px;width:430px}
.box h3{font-family:"Cormorant Garamond",serif;font-size:20px;letter-spacing:.15em;font-weight:400;border-bottom:2px solid var(--teal);padding-bottom:2px}
.box h3 small{font-family:"Noto Sans JP",sans-serif;font-size:10px;color:var(--ink-soft);margin-left:10px;letter-spacing:0}
.box ul{list-style:none;margin-top:8px}
.box li{font-size:11px;line-height:34px;border-bottom:1px solid var(--line);display:flex;gap:16px}
.box li time{color:var(--ink-soft)}
.box .more{margin:16px 0 0 auto}

/* voice */
.voice{left:232px;top:3256px;width:896px}
.voice h3{font-family:"Cormorant Garamond",serif;font-size:20px;letter-spacing:.15em;font-weight:400;border-bottom:1px solid var(--line)}
.voice h3 small{font-family:"Noto Sans JP",sans-serif;font-size:10px;color:var(--ink-soft);margin-left:10px;letter-spacing:0}
.voice-body{display:flex;gap:20px;margin-top:14px}
.voice-body .ph{width:90px;height:60px;background:linear-gradient(135deg,#f4f1ec,#d5c9bc)}
.voice-body p{font-size:11px;line-height:1.9}

/* salon info */
.info{left:232px;top:3500px;width:896px;height:290px;background:var(--cream);padding:20px}
.info-text{left:20px;top:20px;width:230px;font-size:11px;line-height:1.9}
.info-text b{font-family:"Noto Sans JP",sans-serif;font-weight:500;letter-spacing:.12em;font-size:16px;display:block}
.info .p1{left:270px;top:40px;width:150px;height:150px;background:linear-gradient(135deg,#e7ddd0,#9a8470)}
.info .p2{left:428px;top:40px;width:150px;height:150px;background:linear-gradient(135deg,#dfe3d6,#7f8c6e)}
.info .map{left:600px;top:20px;width:276px;height:250px;background:linear-gradient(135deg,#eef0ea,#d8ddd3)}
.info-tel{left:600px;top:20px;background:var(--white);padding:2px 10px;font-weight:700;font-size:15px;display:flex;gap:6px;align-items:center}

/* footer */
.foot-nav{left:0;top:3836px;width:1200px;text-align:center;font-family:"Cormorant Garamond",serif;font-size:12px;letter-spacing:.1em}
.foot-nav span{margin:0 9px}
.copy{left:0;top:3936px;width:1200px;text-align:center;font-size:10px;color:var(--ink-soft)}
</style>
</head>
<body>
<div class="page">

  <aside class="sidebar abs">
    <div class="brand abs"><span class="brand-mark"></span><span class="brand-name">HUELIA</span></div>
    <div class="brand-sub abs">Hair Color Salon</div>
    <div class="reserve abs"><b>Online Reservation</b><span>WEB予約はこちら</span></div>
    <ul class="nav abs">
      <li>HOME</li><li>SALON</li><li>FEATURE</li><li>STAFF</li><li>STYLE</li><li>MENU</li>
      <li>COUPON</li><li>RECRUIT/COMPANY</li><li>NEWS</li><li>BLOG</li><li>VOICE</li>
    </ul>
    <div class="side-banner side-coupon abs"><b>COUPON</b>お得なクーポン</div>
    <div class="side-banner side-snap abs"><span>GUEST SNAP<br>ゲストスナップ</span><span class="ph" role="img" aria-label="ゲストの髪型写真"></span></div>
    <div class="side-banner side-social abs"><i></i>pictabook</div>
  </aside>

  <section class="hero abs">
    <div class="ph" role="img" aria-label="サロンの内装と、カラーリングした髪の女性の写真"></div>
    <div class="hero-copy abs">
      <p>カラー専門サロン「<em>ヒューリア</em>」から提案する</p>
      <p>あなただけの「<em>きれい</em>」を</p>
      <p class="big">低価格・短時間でご提案いたします。</p>
    </div>
    <div class="hero-tag abs">いつもより長めのケアをお約束します</div>
    <div class="hero-tel abs">
      <svg width="16" height="16" viewBox="0 0 24 24"><path fill="#555b5e" d="M6.6 10.8a15 15 0 0 0 6.6 6.6l2.2-2.2c.3-.3.7-.4 1-.2 1.1.4 2.3.6 3.6.6.6 0 1 .4 1 1V20c0 .6-.4 1-1 1A17 17 0 0 1 3 4c0-.6.4-1 1-1h3.5c.6 0 1 .4 1 1 0 1.3.2 2.5.6 3.6.1.3 0 .7-.2 1z"/></svg>
      078-555-0218
    </div>
  </section>

  <section class="feature abs">
    <div class="sec-title"><h2>FEATURE</h2><small>HUELIA の特徴</small></div>
    <p class="lead">毎日綺麗な髪であり続ける為に髪と心のWケア</p>
    <p class="body">ヒューリアはヘアカラーを通じて、髪を傷めず短い時間できれいを手に入れる場所です。ゆったりとした空間で、一人ひとりの髪と心に寄り添うケアをお届けします。お仕事帰りやお子様連れでもお気軽にお立ち寄りください。</p>
  </section>

  <div class="grid abs">
    <div class="tile t1"><h3>安<small>心・安全</small></h3><p>髪と頭皮にやさしい薬剤を厳選し、毎回丁寧に状態を確認しながら施術いたします。</p></div>
    <div class="ph g1" role="img" aria-label="カラー剤を扱う手元の写真"></div>
    <div class="tile t2"><h3>速<small>い</small></h3><p>カラー専門だからこその手際で、お待たせせず短時間で仕上げます。</p></div>
    <div class="ph g2" role="img" aria-label="ブラッシングする女性の髪の写真"></div>
    <div class="ph g3" role="img" aria-label="ヘアケア用品の瓶の写真"></div>
    <div class="tile t3"><h3>低<small>価格</small></h3><p>明瞭な料金設定で、続けやすい価格のカラーをご用意しています。</p></div>
    <div class="ph g4" role="img" aria-label="ヘアカラー施術中の写真"></div>
    <div class="tile t4"><h3>癒<small>し</small></h3><p>落ち着いた空間でゆったりと、心までほぐれるひとときをどうぞ。</p></div>
  </div>
  <div class="more abs" style="left:645px;top:1436px">詳しく見る</div>

  <section class="style abs">
    <div class="sec-title"><h2>STYLE</h2><small>スタイルギャラリー</small></div>
  </section>
  <div class="gallery abs">
    <figure><span class="ph h1" role="img" aria-label="ボブのヘアスタイル写真"></span><figcaption>エアリーボブ・ピンク</figcaption></figure>
    <figure><span class="ph h2" role="img" aria-label="ショートのヘアスタイル写真"></span><figcaption>ナチュラルショート・ベージュ</figcaption></figure>
    <figure><span class="ph h3" role="img" aria-label="ミディアムのヘアスタイル写真"></span><figcaption>大人のミディアムブラウン</figcaption></figure>
    <figure><span class="ph h4" role="img" aria-label="ロングのヘアスタイル写真"></span><figcaption>ゆるふわロング・アッシュ</figcaption></figure>
    <figure><span class="ph h1" role="img" aria-label="ボブのヘアスタイル写真"></span><figcaption>エアリーボブ・ピンク</figcaption></figure>
    <figure><span class="ph h2" role="img" aria-label="ショートのヘアスタイル写真"></span><figcaption>ナチュラルショート・ベージュ</figcaption></figure>
    <figure><span class="ph h3" role="img" aria-label="ミディアムのヘアスタイル写真"></span><figcaption>大人のミディアムブラウン</figcaption></figure>
    <figure><span class="ph h4" role="img" aria-label="ロングのヘアスタイル写真"></span><figcaption>ゆるふわロング・アッシュ</figcaption></figure>
  </div>
  <div class="more abs" style="left:645px;top:2206px">詳しく見る</div>

  <div class="menu-band abs"></div>
  <section class="menu abs">
    <div class="sec-title"><h2>MENU</h2><small>メニュー・料金</small></div>
  </section>
  <div class="menu-cols abs">
    <div class="menu-block"><h4>全体染め<span>根元から毛先まで</span></h4>
      <div class="row"><span>ショート</span><i></i><span>¥3,800</span></div>
      <div class="row"><span>ミディアム</span><i></i><span>¥4,300</span></div>
      <div class="row"><span>ロング</span><i></i><span>¥4,800</span></div></div>
    <div class="menu-block"><h4>根元染め<span>伸びた部分のみ</span></h4>
      <div class="row"><span>根元 2cm</span><i></i><span>¥2,800</span></div>
      <div class="row"><span>根元 4cm</span><i></i><span>¥3,300</span></div>
      <div class="row"><span>生え際のみ</span><i></i><span>¥1,500</span></div></div>
    <div class="menu-block"><h4>外染め<span>表面をおしゃれに</span></h4>
      <div class="row"><span>ハイライト</span><i></i><span>¥3,500</span></div>
      <div class="row"><span>グラデーション</span><i></i><span>¥4,000</span></div>
      <div class="row"><span>ポイントカラー</span><i></i><span>¥2,000</span></div></div>
    <div class="menu-block"><h4>オプション</h4>
      <div class="row"><span>頭皮ケア</span><i></i><span>¥800</span></div>
      <div class="row"><span>トリートメント</span><i></i><span>¥1,000</span></div>
      <div class="row"><span>ブロー</span><i></i><span>¥500</span></div></div>
  </div>
  <div class="more abs" style="left:645px;top:2620px">詳しく見る</div>
  <div class="promo abs">
    <div class="badge abs">初回<br>ご来店</div>
    <div class="txt abs"><small>初めてのご来店の方限定</small><b>カラー(全染め)</b></div>
    <div class="off abs">30<small>%OFF!</small></div>
    <div class="note abs">ご予約の際にクーポンをお伝えください</div>
  </div>

  <div class="box abs" style="left:232px">
    <h3>NEWS<small>新着情報</small></h3>
    <ul>
      <li><time>2015.06.15</time>年末年始の営業日のお知らせ</li>
      <li><time>2015.06.10</time>新メニューを追加いたしました</li>
      <li><time>2015.06.01</time>ウェブサイトを公開しました</li>
    </ul>
    <div class="more">詳しく見る</div>
  </div>
  <div class="box abs" style="left:698px">
    <h3>BLOG<small>ブログ</small></h3>
    <ul>
      <li><time>2015.06.15</time>梅雨時期の髪のお手入れ方法</li>
      <li><time>2015.06.10</time>今季おすすめのカラーをご紹介</li>
      <li><time>2015.06.01</time>スタッフの休日のすごし方</li>
    </ul>
    <div class="more">詳しく見る</div>
  </div>

  <section class="voice abs">
    <h3>VOICE<small>お客様の声</small></h3>
    <div class="voice-body">
      <span class="ph" role="img" aria-label="カウンセリングシートの画像"></span>
      <p>ご来店いただいたお客様に記入していただいたカウンセリングシートをご紹介いたします。<br>2015.06.15　お客様の声を更新しました。</p>
    </div>
  </section>

  <section class="info abs">
    <div class="info-text abs"><b>HUELIA</b>カラー専門サロン ヒューリア<br>〒650-0024<br>神戸市中央区みなと通 2-14-8<br>営業時間 10:00〜19:00<br>定休日 毎週火曜日<br>TEL 078-555-0218</div>
    <span class="ph p1 abs" role="img" aria-label="サロン外観の写真"></span>
    <span class="ph p2 abs" role="img" aria-label="サロン内装の写真"></span>
    <span class="ph map abs" role="img" aria-label="サロン周辺の地図"></span>
    <div class="info-tel abs">
      <svg width="14" height="14" viewBox="0 0 24 24"><path fill="#555b5e" d="M6.6 10.8a15 15 0 0 0 6.6 6.6l2.2-2.2c.3-.3.7-.4 1-.2 1.1.4 2.3.6 3.6.6.6 0 1 .4 1 1V20c0 .6-.4 1-1 1A17 17 0 0 1 3 4c0-.6.4-1 1-1h3.5c.6 0 1 .4 1 1 0 1.3.2 2.5.6 3.6.1.3 0 .7-.2 1z"/></svg>
      078-555-0218
    </div>
  </section>

  <nav class="foot-nav abs">
    <span>HOME</span><span>SALON</span><span>FEATURE</span><span>STAFF</span><span>STYLE</span><span>MENU</span><span>COUPON</span><span>RECRUIT/COMPANY</span><span>NEWS</span><span>BLOG</span><span>VOICE</span><span>GUEST SNAP</span>
  </nav>
  <p class="copy abs">Copyright © HUELIA All Rights Reserved.</p>

</div>
</body>
</html>
```